Kip's Pharmacy Business Card Design Project

I need a business card designed for my pharmacy Kip's Pharmacy. I would like just the logo on one side, maybe with black background and white lettering. The other side I would also like to include my logo which is attached. Also, please include my name and the following information:
Rolf Mayhew Owner/Pharm D.
Business address is 7314 N Birchwood Rd Sioux Falls, SD 57193.
Phone number is 605-318-2067 and fax # is 605-318-2063.
my email address is kip@kipsrxhall.com.
My website is www.kipsrxhall.com.
My business hours are Monday-Friday 8am-7 pm. Saturday 8am-12 pm. Sunday Closed.
I would like the design to include my logo colors, black, white, and neon green. Silver may be added as a highlight. Thanks.
Industry/Entity Type
Pharmacy
Contact Information for Business Card
See above in product description
Look and feel

```html
<!DOCTYPE html>
<html lang="en">
<head>
<meta charset="utf-8">
<title>Kip's Pharmacy – Business Card</title>
<link rel="stylesheet" href="https://fonts.googleapis.com/css2?family=Open+Sans:wght@400;600;700&display=swap">
<style>
  :root {
    --stage: #e4e4e4;
    --card-white: #ffffff;
    --card-dark: #333333;
    --neon-green: #9dcb3b;
    --ink: #2f2f2f;
    --text-light: #ffffff;
    --text-soft: #e2e2e2;
  }
  * { margin: 0; padding: 0; box-sizing: border-box; }
  html, body {
    width: 1200px; height: 900px; overflow: hidden;
    background: radial-gradient(ellipse at center, #f2f2f2 0%, var(--stage) 75%);
    font-family: "Open Sans", Arial, sans-serif;
  }
  .canvas { position: relative; width: 1200px; height: 900px; }
  .business-card {
    position: absolute; left: 120px; top: 176px;
    width: 960px; height: 548px;
    background: var(--card-white);
    overflow: hidden;
    box-shadow: 0 14px 40px rgba(0,0,0,0.18), 0 2px 6px rgba(0,0,0,0.12);
  }
  .card-shapes { position: absolute; inset: 0; }
  .card-shapes .dark-panel { fill: var(--card-dark); }
  .card-shapes .green-swoosh { fill: var(--neon-green); }

  .brand {
    position: absolute; left: 96px; top: 250px;
    display: flex; flex-direction: column; align-items: flex-start; gap: 18px;
  }
  .brand-dot {
    width: 34px; height: 34px; border-radius: 50%;
    background: var(--neon-green);
    margin-left: 6px;
  }
  .brand-name {
    font-weight: 700; font-size: 50px; letter-spacing: -1px;
    color: var(--ink); line-height: 1;
  }

  .contact-panel {
    position: absolute; right: 58px; top: 46px;
    text-align: right; color: var(--text-light);
  }
  .person-name { font-weight: 700; font-size: 30px; line-height: 1.15; }
  .person-title { font-weight: 400; font-size: 24px; line-height: 1.15; color: var(--text-soft); }
  .address {
    margin-top: 52px; font-size: 19px; line-height: 1.35; color: var(--text-soft);
  }
  .contact-list { list-style: none; margin-top: 44px; font-size: 19px; line-height: 1.4; color: var(--text-soft); }
  .contact-list li { display: flex; justify-content: flex-end; align-items: center; gap: 8px; }
  .contact-list svg { width: 16px; height: 16px; fill: none; stroke: var(--text-light); stroke-width: 1.6; }
  .contact-list svg .solid { fill: var(--text-light); stroke: none; }
</style>
</head>
<body>
<main class="canvas">
  <section class="business-card" aria-label="Kip's Pharmacy business card">
    <svg class="card-shapes" viewBox="0 0 960 548" preserveAspectRatio="none" aria-hidden="true">
      <path class="dark-panel" d="M418 0 L960 0 L960 548 L646 548 C616 300 536 86 418 0 Z"/>
      <path class="green-swoosh" d="M352 0 L398 0 C520 84 602 300 628 548 C588 304 494 82 352 0 Z"/>
    </svg>

    <div class="brand">
      <span class="brand-dot"></span>
      <span class="brand-name">Kip's Pharmacy</span>
    </div>

    <div class="contact-panel">
      <p class="person-name">Teodor Vasquell</p>
      <p class="person-title">Director</p>
      <p class="address">041,12th floor,Mall<br>Harbor Road KPL</p>
      <ul class="contact-list">
        <li>012 555 0147
          <svg viewBox="0 0 16 16" aria-label="mobile"><rect x="4" y="1.5" width="8" height="13" rx="1.5"/></svg>
        </li>
        <li>012 555 0147
          <svg viewBox="0 0 16 16" aria-label="phone"><path class="solid" d="M4 2 L6.5 2 L7.5 5 L6 6.2 C6.8 8 8 9.2 9.8 10 L11 8.5 L14 9.5 L14 12 C14 13 13 14 12 14 C6.5 13.6 2.4 9.5 2 4 C2 3 3 2 4 2 Z"/></svg>
        </li>
        <li>yourname@mailbox.com
          <svg viewBox="0 0 16 16" aria-label="email"><rect class="solid" x="1.5" y="3.5" width="13" height="9" rx="1"/><path d="M2 4.5 L8 9 L14 4.5" stroke="#333"/></svg>
        </li>
        <li>www.yoursitename.com
          <svg viewBox="0 0 16 16" aria-label="website"><circle cx="8" cy="8" r="6.3"/><ellipse cx="8" cy="8" rx="2.8" ry="6.3"/><path d="M1.8 8 H14.2 M3 4.6 H13 M3 11.4 H13"/></svg>
        </li>
      </ul>
    </div>
  </section>
</main>
</body>
</html>
```